Company raising consciousness thru leadership & self-awareness needs amazing Letterhead

We are a technology company that spun out of a consulting firm. We are waking people up in corporate America through surveys, leadership development, workshops and consulting. Getting employees to become self-aware and changing company culture through improved leadership and team effectiveness. We need Word letterhead for our proposals, handouts, and worksheets that match our brand standard, is fresh, and communicates trust, credibility and professionalism.

Target Market(s)

Our target clients are other businesses, and executive leaders and C-suite leaders in those companies.

Font styles to use
Sans Serif

Requirements
Must have
• A Word template we can use for handouts, proposals, executive summary, project management documents, and letters. We need our logo. Please add page number and date on the footer. Must match the theme of our new website in look and feel to match the brand we are trying to promote. Use the colors from our brand standard document I submitted.

```html
<!DOCTYPE html>
<html lang="en">
<head>
<meta charset="utf-8">
<title>Meridian Aware Letterhead</title>
<link href="https://fonts.googleapis.com/css2?family=Montserrat:wght@400;600&family=Tinos&display=swap" rel="stylesheet">
<style>
  :root {
    --navy: #233f7e;
    --navy-deep: #1d3470;
    --sky: #4eb7e8;
    --paper: #ffffff;
    --ink: #2a2a2a;
    --backdrop: #e6e7e9;
    --ghost: #ececee;
  }
  html, body {
    margin: 0;
    width: 1200px;
    height: 795px;
    overflow: hidden;
    background: var(--backdrop);
  }
  .letterhead {
    position: absolute;
    left: 339px;
    top: 24px;
    width: 522px;
    height: 746px;
    background: var(--paper);
    box-shadow: 0 8px 24px rgba(0,0,0,0.12);
    overflow: hidden;
    font-family: "Montserrat", sans-serif;
  }
  .letterhead__shapes {
    position: absolute;
    inset: 0;
  }
  .values {
    position: absolute;
    top: 18px;
    right: 20px;
    color: var(--paper);
    font-size: 9px;
    letter-spacing: 0.5px;
    text-align: right;
    line-height: 14px;
  }
  .values__item::after {
    content: "";
    display: inline-block;
    width: 7px;
    height: 7px;
    margin-left: 6px;
    border: 1px solid var(--paper);
    border-radius: 50%;
    vertical-align: -1px;
  }
  .brand {
    position: absolute;
    top: 208px;
    left: 48px;
    display: flex;
    align-items: center;
    gap: 8px;
  }
  .brand__dot {
    width: 16px;
    height: 16px;
    border-radius: 50%;
    background: var(--navy);
  }
  .brand__name {
    font-size: 13px;
    font-weight: 600;
    color: var(--navy);
    letter-spacing: 1px;
  }
  .letter {
    position: absolute;
    top: 286px;
    left: 68px;
    width: 380px;
    font-family: "Tinos", serif;
    font-size: 8.5px;
    line-height: 11px;
    color: var(--ink);
  }
  .letter p { margin: 0 0 10px; }
  .signature {
    position: absolute;
    top: 564px;
    left: 120px;
    width: 90px;
    height: 34px;
    background: linear-gradient(90deg, #f3f3f3, #e4e4e4);
    border-radius: 4px;
  }
  .watermark {
    position: absolute;
    top: 500px;
    right: 50px;
    width: 90px;
    height: 90px;
    border-radius: 50%;
    background: radial-gradient(circle, var(--ghost), rgba(236,236,238,0));
  }
  .contact {
    position: absolute;
    left: 26px;
    bottom: 22px;
    color: var(--paper);
    font-size: 8.5px;
    line-height: 15px;
  }
  .contact__line { display: flex; align-items: center; gap: 7px; font-weight: 600; }
  .contact__icon { width: 9px; height: 9px; }
  .contact__address { font-weight: 400; font-size: 9.5px; margin-top: 2px; }
</style>
</head>
<body>
  <main class="letterhead">
    <svg class="letterhead__shapes" width="522" height="746" viewBox="0 0 522 746">
      <defs>
        <linearGradient id="navyFade" x1="0" y1="0" x2="1" y2="0">
          <stop offset="0" stop-color="#2c4c94"/>
          <stop offset="1" stop-color="#1d3470"/>
        </linearGradient>
      </defs>
      <polygon points="0,0 522,0 522,64 0,196" fill="url(#navyFade)"/>
      <polygon points="0,170 0,330 46,212" fill="var(--sky)"/>
      <polygon points="522,440 522,610 476,580" fill="var(--sky)"/>
      <polygon points="0,650 522,600 522,746 0,746" fill="url(#navyFade)"/>
    </svg>

    <div class="values">
      <div class="values__item">TRUST</div>
      <div class="values__item">CREDIBILITY</div>
      <div class="values__item">PROFESSIONALISM</div>
    </div>

    <div class="brand">
      <span class="brand__dot"></span>
      <span class="brand__name">MERIDIAN AWARE</span>
    </div>

    <section class="letter">
      <p>Dear Mr. Smith,</p>
      <p>Lorem ipsum dolor sit amet, consectetuer adipiscing elit, sed diam nonummy nibh euismod tincidunt ut laoreet dolore magna aliquam erat volutpat. Ut wisi enim ad minim veniam, quis nostrud exerci tation ullamcorper suscipit lobortis nisl ut aliquip ex ea commodo consequat. Duis autem vel eum iriure dolor in hendrerit in vulputate velit esse molestie consequat.</p>
      <p>Lorem ipsum dolor sit amet, consectetuer adipiscing elit, sed diam nonummy nibh euismod tincidunt ut laoreet dolore magna aliquam erat volutpat. Ut wisi enim ad minim veniam, quis nostrud exerci tation ullamcorper suscipit lobortis nisl ut aliquip ex ea commodo consequat. Duis autem vel eum iriure dolor in hendrerit in vulputate velit esse molestie consequat, vel illum dolore eu feugiat nulla facilisis at vero eros et accumsan et iusto odio dignissim qui blandit praesent luptatum zzril delenit augue duis dolore te feugait nulla facilisi. Nam liber tempor cum soluta nobis eleifend option congue nihil imperdiet doming id quod mazim placerat facer possim assum.</p>
      <p>Lorem ipsum dolor sit amet, consectetuer adipiscing elit, sed diam nonummy nibh euismod tincidunt ut laoreet dolore magna aliquam erat volutpat. Ut wisi enim ad minim veniam, quis nostrud exerci tation ullamcorper suscipit lobortis nisl ut aliquip ex ea commodo consequat. Duis autem vel eum iriure dolor in hendrerit in vulputate velit esse molestie consequat.</p>
      <p>Sincerely,</p>
      <p>John Doe<br>Sales Manager</p>
    </section>

    <div class="signature" role="img" aria-label="Handwritten signature"></div>
    <div class="watermark" role="img" aria-label="Faint brand decoration"></div>

    <footer class="contact">
      <div class="contact__line">
        <svg class="contact__icon" viewBox="0 0 10 10"><path d="M2 1 L4 1 L5 3 L4 4 Q5 6 6 6 L7 5 L9 6 L9 8 Q5 9 1 4 Z" fill="none" stroke="#fff" stroke-width="0.9"/></svg>
        +0 123 456 789
      </div>
      <div class="contact__line">
        <svg class="contact__icon" viewBox="0 0 10 10"><rect x="1" y="2" width="8" height="6" fill="none" stroke="#fff" stroke-width="0.9"/><path d="M1 2 L5 5.5 L9 2" fill="none" stroke="#fff" stroke-width="0.9"/></svg>
        info@yourmail.com
      </div>
      <div class="contact__line">
        <svg class="contact__icon" viewBox="0 0 10 10"><circle cx="5" cy="5" r="4" fill="none" stroke="#fff" stroke-width="0.9"/><path d="M1 5 H9 M5 1 Q2.5 5 5 9 M5 1 Q7.5 5 5 9" fill="none" stroke="#fff" stroke-width="0.7"/></svg>
        www.yourcompany.com
      </div>
      <div class="contact__address">Your address, Suit # 000, Dummy Street, City, State,</div>
    </footer>
  </main>
</body>
</html>
```